Window Cleaning Flyer targeting Shopfronts and Small Commercial Work

Single page flyer similar to the flyer targeting small commercial work and shopfronts

Please include the following text:

Brisk Pane Services delivers high quality service to suburbs all around Melbourne. From Frankston to Kalkallo, Brisk has you covered!

With over 10 years experience, Brisk specialises in providing:
- Window Cleaning: via elevated work platforms, rope access and extension poles
- Pressure Cleaning: Including chlorine treatment to prevent mould regrowth on concrete area
- Roof Gutter Cleaning: using our ladder free gutter vacuum

We pride ourselves on neat and professional presentation and vast geographical reach across Melbourne.

Our services can be completed on a frequency that meets your window cleaning needs. Whether a weekly clean or a yearly service.

Brisk Pane Services Melbourne takes care of all your window cleaning needs.

Contact Us now for free quote!

Target Market(s)

Small business and commercial building owners

Industry/Entity Type

Window Cleaning

Requirements
Must have
• Only use photos/logos provided
Should not have
• Stock phots

```html
<!DOCTYPE html>
<html lang="en">
<head>
<meta charset="utf-8">
<title>Brisk Pane Services – Flyer</title>
<link href="https://fonts.googleapis.com/css2?family=Arimo:wght@400;700&display=swap" rel="stylesheet">
<style>
  :root {
    --page-bg: #e8e5e1;
    --brand-blue: #0d4f8b;
    --text-blue: #0c4a87;
    --brand-yellow: #f7e926;
    --ink: #2b2b2b;
    --white: #ffffff;
  }
  * { box-sizing: border-box; margin: 0; padding: 0; }
  html, body {
    width: 1200px; height: 1200px; overflow: hidden;
    background: var(--page-bg);
    font-family: "Arimo", Arial, sans-serif;
  }
  .flyer {
    position: absolute; left: 199px; top: 30px;
    width: 802px; height: 1140px;
    background: var(--white);
    box-shadow: 0 6px 18px rgba(0,0,0,0.25);
    overflow: hidden;
  }
  .hero-photo {
    position: absolute; left: 0; top: 0; width: 802px; height: 414px;
    background: linear-gradient(90deg, #a34e3b 0%, #8a4233 35%, #3a3330 55%, #4a3f3a 72%, #5d7a42 88%, #8aa66a 100%);
  }
  .intro-panel {
    position: absolute; left: 0; top: 82px; width: 560px; height: 251px;
    background: linear-gradient(90deg, var(--brand-blue) 0%, var(--brand-blue) 72%, rgba(13,79,139,0) 100%);
    padding: 24px 0 0 34px;
    color: var(--white);
  }
  .brand-name {
    font-weight: 700; font-size: 38px; line-height: 1;
    color: var(--brand-yellow);
    letter-spacing: 0.5px;
    text-transform: uppercase;
  }
  .intro-text {
    margin-top: 32px; font-size: 18px; line-height: 23px; width: 380px;
  }
  .services-card {
    position: absolute; left: 55px; top: 392px; width: 298px; height: 276px;
    background: var(--brand-yellow);
    padding: 14px 14px 0 24px;
    color: var(--text-blue);
    font-size: 16.5px; line-height: 23px;
    border-radius: 0 0 3px 3px;
  }
  .services-tabs { position: absolute; left: 38px; top: 392px; width: 336px; height: 22px; }
  .services-card .lead { font-weight: 700; }
  .services-card ul { list-style: none; }
  .services-card li::before { content: "\25CF"; color: #1a1a1a; font-size: 13px; margin-right: 12px; }
  .card-shadow {
    position: absolute; left: 62px; top: 670px; width: 284px; height: 10px;
    background: radial-gradient(ellipse at top, rgba(0,0,0,0.22), rgba(0,0,0,0) 70%);
  }
  .frequency-text {
    position: absolute; left: 401px; top: 446px; width: 370px;
    color: var(--text-blue); font-size: 18.5px; line-height: 23px;
  }
  .work-photo {
    position: absolute; left: 414px; top: 570px; width: 340px; height: 407px;
    border: 2px solid var(--white);
    box-shadow: 0 3px 8px rgba(0,0,0,0.3);
    background: linear-gradient(180deg, #9fb79c 0%, #6b4a33 18%, #4f7a6a 40%, #5e4030 60%, #9b6a4a 80%, #7a5240 100%);
  }
  .pride-text {
    position: absolute; left: 35px; top: 709px; width: 338px;
    color: var(--ink); font-size: 22px; line-height: 27px; text-align: justify;
  }
  .tagline {
    position: absolute; left: 35px; top: 845px; width: 338px;
    color: var(--text-blue); font-size: 23.5px; line-height: 30.5px;
    text-align: center; text-transform: uppercase;
  }
  .contact-band {
    position: absolute; left: 0; top: 1017px; width: 802px; height: 123px;
    background: var(--brand-blue); color: var(--white);
  }
  .contact-cta {
    position: absolute; left: 50px; top: 40px;
    font-weight: 700; font-size: 22px;
  }
  .contact-phone {
    position: absolute; right: 37px; top: 24px;
    font-weight: 700; font-size: 47px; line-height: 1;
  }
  .contact-address {
    position: absolute; right: 37px; top: 84px;
    font-weight: 700; font-size: 13px;
  }
</style>
</head>
<body>
  <article class="flyer">
    <div class="hero-photo" role="img" aria-label="Photo of a technician on an elevated work platform cleaning high windows of a brick building beside trees"></div>

    <header class="intro-panel">
      <div class="brand-name">Brisk Pane Services</div>
      <p class="intro-text">Brisk Pane Services delivers high quality service to suburbs all around Melbourne.<br>From Frankston to Kalkallo, Brisk has you covered!</p>
    </header>

    <svg class="services-tabs" viewBox="0 0 336 22" aria-hidden="true">
      <polygon points="0,22 17,0 17,22" fill="#f7e926"/>
      <polygon points="319,0 336,22 319,22" fill="#f7e926"/>
    </svg>
    <section class="services-card">
      <p class="lead">With over 10 years experience, Brisk specialises in providing:</p>
      <ul>
        <li>Window Cleaning: via elevated work platforms, rope access and extension poles</li>
        <li>Pressure Cleaning: Including chlorine treatment to prevent mould regrowth on concrete area</li>
        <li>Roof Gutter Cleaning: using our ladder free gutter vacuum</li>
      </ul>
    </section>
    <div class="card-shadow"></div>

    <p class="frequency-text">Our services can be completed on a frequency that meets your window cleaning needs. Whether a weekly clean or a yearly service.</p>

    <div class="work-photo" role="img" aria-label="Photo of a cleaner using a long extension pole to clean upper windows of a two-storey house with a balcony"></div>

    <p class="pride-text">We pride ourselves on neat and professional presentation and vast geographical reach across Melbourne.</p>

    <p class="tagline">Brisk Pane Services Melbourne takes care of all your window cleaning needs</p>

    <footer class="contact-band">
      <div class="contact-cta">Contact Us now for free quote!</div>
      <div class="contact-phone">+61 3 9000 4821</div>
      <div class="contact-address">PO BOX 2740 &#9679; Boxwood North, Victoria, Australia</div>
    </footer>
  </article>
</body>
</html>
```